Saucy Velvet Kittenz Business Card

We need business cards designed for our consultants to use and hand out to customers.
We are an Adult party plan company (like Crispaboxa but sex toys and lingerie)
We would like bright colours pinks, purples.
The cards need our logo
Space for the reps phone number email address and name.
We need our website on it www.saucyvelvetkittens.com.au

```html
<!DOCTYPE html>
<html lang="en">
<head>
<meta charset="utf-8">
<title>Saucy Velvet Kittenz Business Card</title>
<link rel="stylesheet" href="https://fonts.googleapis.com/css2?family=Arvo:wght@700&family=Kalam:wght@300&family=Arimo:wght@400&display=swap">
<style>
  :root {
    --backdrop: #e4e2de;
    --card: #0b0b0b;
    --pink: #e83e8c;
    --white: #ffffff;
  }
  * { margin: 0; padding: 0; box-sizing: border-box; }
  html, body { width: 1200px; height: 1000px; overflow: hidden; }
  body {
    background: var(--backdrop);
    display: flex;
    align-items: center;
    justify-content: center;
    gap: 90px;
  }
  .card {
    position: relative;
    width: 340px;
    height: 590px;
    background: var(--card);
    border-radius: 4px;
    box-shadow: 0 10px 28px rgba(0,0,0,0.25);
    overflow: hidden;
  }
  .tagline {
    position: absolute;
    top: 46px;
    left: 40px;
    right: 40px;
    font-family: "Kalam", cursive;
    font-weight: 300;
    font-size: 30px;
    line-height: 1.15;
    color: var(--pink);
    text-align: center;
  }
  .logo-figure {
    position: absolute;
    top: 170px;
    left: 95px;
    width: 150px;
    height: 240px;
    border-radius: 70px 70px 20px 20px;
    background: linear-gradient(180deg, #ef5a9e, #d42f7c);
    opacity: 0.85;
  }
  .brand-name {
    position: absolute;
    left: 0;
    right: 0;
    bottom: 80px;
    font-family: "Arvo", serif;
    font-weight: 700;
    font-size: 24px;
    line-height: 1.3;
    color: var(--white);
    text-align: center;
  }
  .claim {
    position: absolute;
    top: 40px;
    left: 36px;
    right: 36px;
    font-family: "Arvo", serif;
    font-weight: 700;
    font-size: 23px;
    line-height: 1.2;
    color: var(--white);
  }
  .tail-art {
    position: absolute;
    top: 120px;
    left: 60px;
    width: 220px;
    height: 160px;
    border-radius: 50%;
    background: radial-gradient(ellipse at center, rgba(232,62,140,0.45), rgba(232,62,140,0) 70%);
  }
  .rep-name {
    position: absolute;
    top: 300px;
    left: 36px;
    font-family: "Kalam", cursive;
    font-weight: 300;
    font-size: 40px;
    color: var(--pink);
  }
  .contact {
    position: absolute;
    left: 36px;
    bottom: 44px;
    list-style: none;
    font-family: "Arimo", sans-serif;
    font-size: 17px;
    line-height: 1.75;
    color: var(--white);
  }
</style>
</head>
<body>
  <section class="card card-front">
    <p class="tagline">Making the world<br>a hornier place!</p>
    <div class="logo-figure" role="img" aria-label="Brand figure illustration in pink"></div>
    <p class="brand-name">Saucy Velvet Kittenz<br>Parties</p>
  </section>

  <section class="card card-back">
    <p class="claim">Australia's No 1<br>Adult Party Plan</p>
    <div class="tail-art" role="img" aria-label="Pink decorative flourish"></div>
    <p class="rep-name">Mara Ellison</p>
    <ul class="contact">
      <li>0400 316 820</li>
      <li>mara@saucyvelvetkittens.com.au</li>
      <li>www.saucyvelvetkittens.com.au</li>
      <li>social/maraellison</li>
    </ul>
  </section>
</body>
</html>
```